Hair Extension Aftercare sheet

This sheet is to give to customers regarding the aftercare of hair extensions. There should be Simple and minimal look - approx A5 size and can be folded to suit. I have attached the content and logo files for use.
We are not looking for to much artwork just clean, professional look.
All the content provided in a compact flyer format i.e
A foldable A5 pamphlet or the like, this is for packaging requirements
Please do not submit A4 layouts

Industry/Entity Type

Hair And Beauty

Requirements
Must have
• All the content provided in a compact flyer format i.e
• A foldable A5 pamphlet or the like, this is for packaging requirements
Should not have
• tacky art work or images - must be clean lines

```html
<!DOCTYPE html>
<html lang="en">
<head>
<meta charset="utf-8">
<title>Hair Extension Aftercare Sheet</title>
<link href="https://fonts.googleapis.com/css2?family=EB+Garamond:wght@400&family=Arimo:wght@400&display=swap" rel="stylesheet">
<style>
  :root {
    --paper: #ffffff;
    --ink: #231f20;
    --heading: #5a4810;
    --alert: #e3241b;
    --photo-dark: #7a4a22;
    --photo-mid: #b07a45;
    --photo-light: #e9d3bd;
  }
  * { margin: 0; padding: 0; box-sizing: border-box; }
  html, body { width: 1200px; height: 848px; overflow: hidden; background: var(--paper); }
  .sheet { position: relative; width: 1200px; height: 848px; background: var(--paper); color: var(--ink); }
  .block { position: absolute; width: 290px; }
  .col-1 { left: 22px; }
  .col-2 { left: 326px; width: 258px; }
  .col-3 { left: 609px; width: 274px; }
  .col-4 { left: 898px; width: 282px; }
  .body-text {
    font-family: "EB Garamond", Garamond, serif;
    font-size: 12.6px;
    line-height: 17.05px;
    text-align: justify;
    hyphens: none;
  }
  .section-title {
    font-family: "Arimo", Arial, sans-serif;
    font-size: 14px;
    line-height: 17.5px;
    color: var(--heading);
    text-decoration: underline;
    text-underline-offset: 2px;
    text-decoration-thickness: 1.5px;
  }
  .alert {
    font-family: "Arimo", Arial, sans-serif;
    font-size: 14px;
    line-height: 17.2px;
    color: var(--alert);
  }
  .alert.justified { text-align: justify; }
  .portrait {
    position: absolute; left: 912px; top: 328px; width: 196px; height: 278px;
    border-radius: 48% 48% 30% 30% / 40% 40% 30% 30%;
    background: radial-gradient(ellipse at 50% 30%, var(--photo-mid), var(--photo-dark) 60%, var(--photo-light) 100%);
  }
</style>
</head>
<body>
<main class="sheet">

  <!-- Column one -->
  <h1 class="block col-1 section-title" style="top:20px">AFTERCARE AND MAINTENANCE GUIDELINES</h1>
  <p class="block col-1 body-text" style="top:70px">It is very important to keep this exceptional quality hair in the best condition you can. Please read all of the information below:</p>
  <p class="block col-1 body-text" style="top:137px">It is important to use the right tools for the job. A good hair brush is a small investment to keep your hair in the best possible condition and contributes to a pleasant wearing experience.</p>
  <p class="block col-1 body-text" style="top:218px">Mira Hale Bristle Brushes with small plastic pins and real bristle hair are ideal and specially developed for this purpose. It smooths the hair without loosing brushing grip and removes tangles effortlessly.</p>
  <h2 class="block col-1 section-title" style="top:331px">GENERAL:</h2>
  <p class="block col-1 body-text" style="top:359px">Do not use oil based products, always use water dissolvable products. Oil based products will keep the hair in a wet condition and can cause matting. Oil based products attract a lot more dust and dirt which will make the hair less smooth and feel dry.</p>
  <h2 class="block col-1 section-title" style="top:472px">GENERAL WASHING &amp; CONDITIONING:</h2>
  <p class="block col-1 body-text" style="top:499px">Shampoo at least two times per week. Never wash, brush or dry the hair upside down. Before washing, brush out all tangles with a hair extension brush (available from Mira Hale Hair Extensions). Do not use a brush with only plastic or steel pins. Always start brushing or combing at the ends, working your way up to the roots. possibleWet the hair thoroughly, then dispense a small amount of shampoo into your hand and rub your hands together. Apply the shampoo evenly on the scalp and at the roots. Gently wash the scalp using your fingertips without rubbing the hair. Rinse thoroughly while squeezing the hair to remove all shampoo residue. If the shampoo does not foam the first time, don’t apply more shampoo but continue washing as normal. After rinsing simply re-apply the shampoo for a second time. There is no need to apply a lot of shampoo in the lengths. The hair will get cleaned when you rinse the hair out (unless extremely dirty).</p>

  <!-- Column two -->
  <p class="block col-2 alert justified" style="top:24px;font-size:14.4px">Avoid: Shampoos that contain sulphates &amp; products that are oil based.</p>
  <p class="block col-2 body-text" style="top:87px">If you can’t wash it off your hands without shampoo, it is more likely oil based.</p>
  <h2 class="block col-2 section-title" style="top:145px">AFTER YOU WASHED THE HAIR:</h2>
  <p class="block col-2 body-text" style="top:177px">After washing you may use a conditioner however, apply the conditioner from the ends to half way up the length. Never at the roots. Comb the conditioner through using a large wide tooth comb until all tangles are removed. Rinse thoroughly to leave no residue in the hair. Towel dry the hair by squeezing it with the towel. Don’t rub or massage the hair.</p>
  <p class="block col-2 body-text" style="top:328px">You can apply small amounts of leave-in conditioner or a recommended styling product, comb through with your fingers into the direction you would like your hair to fall and scruntch it upwards once more. After you have done this leave the hair to dry completely without touching, combing or brushing it.Best natural result.</p>
  <p class="block col-2 body-text" style="top:479px">Let it dry naturally or use your favourite styling equipment. Use leave in conditioners only at the ends! When the hair is completely dry.</p>
  <h2 class="block col-2 section-title" style="top:554px">AT NIGHT</h2>
  <p class="block col-2 body-text" style="top:585px">Braid the hair in a large loose braid at the nape of the neck before going to sleep. Do not sleep with wet hair, this will cause tangling and will make it difficult to style the following morning.</p>
  <h2 class="block col-2 section-title" style="top:674px">STYLING THE HAIR</h2>
  <p class="block col-2 body-text" style="top:705px">You can use a ceramic straightening iron or a hair dryer with a bristle brush to smooth the hair. Other styling tools that can be used are: Heated rollers, steam rollers, curling irons, hot air curling tongs and setting rollers.</p>

  <!-- Column three -->
  <p class="block col-3 alert" style="top:25px">IMPORTANT:</p>
  <p class="block col-3 alert" style="top:52px">NEVER USE HOT STYLING EQUIPMENT THAT EXCEEDS 200 DEGREES CELSIUS OR 392 DEGREES FAHRENHEIT.</p>
  <p class="block col-3 body-text" style="top:113px">Temperatures above this can damage the protein in the hair causing it to solidify and make the hair dry and unmanageable. Always keep hot styling equipment moving through the hair and do not hold for too long in one place. We do not recommend using straightening irons on wet hair.</p>
  <h2 class="block col-3 section-title" style="top:241px">SPORTS AND OTHER ACTIVITIES</h2>
  <p class="block col-3 body-text" style="top:268px">Don’t expose your hair to strong windy conditions like sailing, motor sports, cabriolet cars. Wear protective head wear. If you sweat a lot during work outs, at least rinse out the saltiness as this will dry out the hair.</p>
  <h2 class="block col-3 section-title" style="top:377px">VISITING SAUNAS AND STEAM ROOMS</h2>
  <p class="block col-3 body-text" style="top:418px">Braid the hair in a loose braid in the nape of the neck and put it up using a hair clip. The hair can get very hot and can be painful when it touches the skin just like your own natural hair. Only brush the hair when it is cooled down. After the sauna rinse the hair under the shower and preferably wash the hair and condition it at the end of the visit or when you get home as stated in this aftercare sheet.</p>
  <h2 class="block col-3 section-title" style="top:596px">SWIMMING</h2>
  <p class="block col-3 body-text" style="top:627px">It is not recommended that you swim while wearing curly, deep curly and deep curl textures, you can swim but don’t submerge your head in the water. If you swim every day or frequently, other textures are more suitable. Other textures before swimming, brush out any tangles. Make one braid at the nape of your neck. Try to keep your hair out of the water as much as possible. After swimming in chlorinated water or sea water, undo the braid and rinse immediately under the shower.</p>

  <!-- Column four -->
  <p class="block col-4 body-text" style="top:24px">This is very important to rinse out all of the chlorine or salt, both will dry your hair out when you leave it in for too long. Condition and comb out with a wide tooth comb, then leave to dry naturally. Wash and condition the hair as soon as possible as recommended in this guide.</p>
  <h2 class="block col-4 section-title" style="top:142px">SUNBATHING</h2>
  <p class="block col-4 body-text" style="top:169px">Braid your hair in a large braid at the back of the neck. After sunbathing, do not undo the braid until the hair cools down.</p>
  <h2 class="block col-4 section-title" style="top:245px">TANNING MACHINES</h2>
  <p class="block col-4 body-text" style="top:272px">Whilst laying under a tanning machine, cover the hair loosely with a towel. Don’t apply skin tan oil or sunblock to the hair.</p>
  <div class="portrait" role="img" aria-label="Photograph of a styling mannequin head with auburn hair in a rose-curl updo and drop earrings"></div>
  <h2 class="block col-4 section-title" style="top:618px">GENERAL DAILY STYLING GUIDE</h2>
  <p class="block col-4 body-text" style="top:650px">In the morning undo the braid and brush the hair starting from the ends upwards to the roots until all tangles are removed. If necessary, dampen the hair with a water spray. You can use a ceramic hair straightening iron (NOT ON DAMP OR WET HAIR) or a hair dryer with an extension brush to smooth the hair. Other styling tools that can be used are: Heated rollers, steam rollers, curling irons, hot air curling tongs and setting rollers.</p>

</main>
</body>
</html>
```